Cybersecurity company is looking for business card.

I need a business card design for our company, we are a cybersecurity company providing advance technology to protect agains any kind of malware. We need a fresh modern design it should communicate modern, technology and growth.

Target Market(s)

Business to business

Industry/Entity Type

Business

Contact Information for Business Card

Should have location, address, fax, mobile, phone, email and website.

Requirements
Must have
• Must follow company's logo color and style. Must have the company's log on its.

```html
<!DOCTYPE html>
<html lang="en">
<head>
<meta charset="utf-8">
<title>Veltrix Business Card</title>
<link rel="stylesheet" href="https://fonts.googleapis.com/css2?family=Open+Sans:wght@400;700&display=swap">
<style>
  :root {
    --stage: #141414;
    --card-white: #efefef;
    --card-white-edge: #d9d9d9;
    --brand-red: #9c1a1e;
    --brand-red-dark: #6e1013;
    --ink: #141414;
    --label-grey: #9a9a9a;
    --value-white: #f4f4f4;
  }
  * { margin: 0; padding: 0; box-sizing: border-box; }
  html, body { width: 1200px; height: 900px; overflow: hidden; background: var(--stage); }
  body { font-family: "Open Sans", Verdana, sans-serif; position: relative; }

  .card {
    position: absolute;
    width: 630px;
    height: 360px;
    overflow: hidden;
    box-shadow: 0 18px 40px rgba(0,0,0,0.6);
  }
  .card__shapes { position: absolute; inset: 0; width: 100%; height: 100%; }

  .card--back { left: 110px; top: 50px; }
  .card--back .brand-name {
    position: absolute;
    left: 120px; top: 110px;
    font-size: 104px;
    font-weight: 700;
    letter-spacing: 2px;
    color: var(--ink);
    line-height: 1;
  }
  .card--back .address {
    position: absolute;
    right: 40px; top: 250px;
    font-size: 14px;
    color: var(--ink);
  }

  .card--front { left: 460px; top: 490px; }
  .card--front .brand-name {
    position: absolute;
    left: 46px; top: 60px;
    font-size: 42px;
    font-weight: 700;
    letter-spacing: 1px;
    color: var(--ink);
    line-height: 1;
  }
  .contact-list {
    position: absolute;
    left: 270px; top: 150px;
    list-style: none;
    font-size: 19px;
    line-height: 26px;
  }
  .contact-list .label { color: var(--label-grey); }
  .contact-list .value { color: var(--value-white); }
</style>
</head>
<body>

  <section class="card card--back" aria-label="Card back">
    <svg class="card__shapes" viewBox="0 0 630 360" preserveAspectRatio="none" aria-hidden="true">
      <defs>
        <linearGradient id="backWhite" x1="0" y1="0" x2="1" y2="1">
          <stop offset="0" stop-color="#f7f7f7"/>
          <stop offset="1" stop-color="#d6d6d6"/>
        </linearGradient>
      </defs>
      <rect width="630" height="360" fill="url(#backWhite)"/>
      <polygon points="0,190 110,170 40,360 0,360" fill="var(--brand-red)"/>
    </svg>
    <div class="brand-name">veltrix</div>
    <p class="address">Tower 4, Harbor Road, Dubai-UAE</p>
  </section>

  <section class="card card--front" aria-label="Card front">
    <svg class="card__shapes" viewBox="0 0 630 360" preserveAspectRatio="none" aria-hidden="true">
      <defs>
        <linearGradient id="frontWhite" x1="0" y1="0" x2="1" y2="1">
          <stop offset="0" stop-color="#f2f2f2"/>
          <stop offset="1" stop-color="#d9d9d9"/>
        </linearGradient>
        <radialGradient id="frontRed" cx="0.45" cy="0.35" r="0.8">
          <stop offset="0" stop-color="#a81d22"/>
          <stop offset="1" stop-color="var(--brand-red-dark)"/>
        </radialGradient>
      </defs>
      <rect width="630" height="360" fill="url(#frontWhite)"/>
      <polygon points="420,0 630,0 630,360 70,360" fill="url(#frontRed)"/>
    </svg>
    <div class="brand-name">veltrix</div>
    <ul class="contact-list">
      <li><span class="label">mobile:</span> <span class="value">+971 50 555 0147</span></li>
      <li><span class="label">phone:</span> <span class="value">04 555 0162</span></li>
      <li><span class="label">fax:</span> <span class="value">04 555 0163</span></li>
      <li><span class="label">email:</span> <span class="value">name.surname@veltrix.com</span></li>
      <li><span class="label">website:</span> <span class="value">www.veltrix.com</span></li>
    </ul>
  </section>

</body>
</html>
```